Established research company needs fresh new powerpoint template

We need a powerpoint template for an established research and advisory company called Veltra Consulting. We develop policy, improve delivery, and build capacity within the public sector - mainly in relation to education and young people.

We have a long and successful track record in our sector, and have a grown-up, clean brand. We already have a logo (see attached) and want a simple, clean powerpoint template that incorporates our logo and colours and matches the brand identity on our website: https://www.veltraconsulting.example/

We need a title slide, a section header slide, a two-column slide for two panels of text, a two-column slide for one panel of text and one panel of imagery, and a single-column slide for text.

We want a template with built-in Styles so our team can make consistent-looking presentations without any manual formatting. We also want to use a font that will be compatible with devices used across a range of clients.

```html
<!DOCTYPE html>
<html lang="en">
<head>
<meta charset="utf-8">
<title>Veltra Consulting – Presentation Template</title>
<link href="https://fonts.googleapis.com/css2?family=Montserrat:wght@400;500;600;700;800&display=swap" rel="stylesheet">
<style>
:root{
  --blue:#0b4d8e;
  --blue-deep:#0a447e;
  --orange:#f07f2d;
  --sky:#7fb2de;
  --grey-text:#8b9099;
  --grey-soft:#e9eaed;
  --board:#e3e5e9;
  --white:#ffffff;
}
*{margin:0;padding:0;box-sizing:border-box}
html,body{width:1200px;height:1169px;overflow:hidden;background:var(--board);font-family:'Montserrat',Arial,sans-serif}
.board{position:absolute;left:0;top:0;width:1954px;height:1904px;transform:scale(.61412);transform-origin:0 0}
.slide{position:absolute;width:600px;height:338px;background:var(--white);overflow:hidden;box-shadow:0 4px 10px rgba(0,0,0,.18)}
.abs{position:absolute}
.rail{position:absolute;left:0;top:0;width:37px;height:100%;background:var(--blue);z-index:3}
.rail span{position:absolute;left:50%;top:50%;transform:translate(-50%,-50%) rotate(90deg);white-space:nowrap;font-size:9px;letter-spacing:2.4px;color:var(--white);font-weight:500}
.rail.light{background:var(--white)}
.rail.light span{color:var(--grey-text)}
.deco{position:absolute;width:74px;height:74px;border-radius:50%;background:var(--grey-soft)}
.brand{position:absolute;right:14px;top:14px;font-size:12px;font-weight:700;color:var(--grey-text);line-height:1;z-index:4}
.brand.on-blue{color:#c9d4e3}
.title{position:absolute;font-size:22px;font-weight:800;color:var(--blue);line-height:1.2}
.rule{position:absolute;width:40px;height:3px;background:var(--orange)}
.body{position:absolute;font-size:7px;line-height:1.45;color:var(--grey-text);text-align:justify}
.body p+p{margin-top:8px}
.accent{color:var(--orange);font-weight:600}
.strong-blue{color:var(--blue);font-weight:700}
.photo{position:absolute}
.toc-item{position:absolute;width:210px}
.toc-item h3{font-size:11px;font-weight:600;color:var(--orange)}
.toc-item h3 b{color:var(--blue);margin-right:6px}
.toc-item p{font-size:6px;color:var(--grey-text);margin:5px 0 0 18px;line-height:1.5}
.badge{position:absolute;width:50px;height:50px;border-radius:50%;background:#cfe2f3;display:flex;align-items:center;justify-content:center}
.badge i{width:40px;height:40px;border-radius:50%;background:#3d86c8;display:flex;align-items:center;justify-content:center;color:#fff;font-style:normal;font-weight:700;font-size:16px;border:2px solid #fff}
.feature{position:absolute;width:100px;text-align:center}
.feature h4{font-size:8.5px;font-weight:700;color:var(--blue)}
.feature h4.alt{color:var(--orange)}
.feature p{font-size:5.5px;color:var(--grey-text);line-height:1.4;margin-top:2px}
.edu-box{position:absolute;width:100px;height:150px;border:3px solid var(--white);border-radius:12px;text-align:center;color:var(--white);padding:24px 10px 0}
.edu-box h4{font-size:9px;font-weight:600;color:var(--orange);margin:6px 0 8px}
.edu-box p{font-size:5.5px;line-height:1.35}
.legend{position:absolute;width:120px}
.legend h5{font-size:7.5px;font-weight:600;color:var(--orange);display:flex;align-items:center;gap:6px}
.legend h5::before{content:"";width:7px;height:7px;border-radius:50%;background:var(--blue)}
.legend h5.dot-orange::before{background:var(--orange)}
.legend p{font-size:4.5px;color:var(--grey-text);line-height:1.4;margin:2px 0 0 13px}
.num-circle{position:absolute;width:38px;height:38px;border-radius:50%;background:var(--orange);color:#fff;font-weight:700;font-size:18px;display:flex;align-items:center;justify-content:center}
.goal-item{position:absolute;left:68px;width:245px;font-size:6.5px;line-height:1.5;color:var(--grey-text)}
.goal-item b{color:var(--blue)}
.goal-item.o b{color:var(--orange)}
.goal-box{position:absolute;left:327px;top:72px;width:273px;height:210px;background:var(--blue);color:#fff;padding:16px 14px}
.goal-box h3{font-size:12.5px;font-weight:600;line-height:1.3;margin-bottom:6px}
.goal-box h3 em{font-style:normal;color:var(--orange);font-weight:800}
.goal-box li{list-style:none;font-size:11px;line-height:1.82;display:flex;align-items:center;gap:8px;padding-left:8px}
.goal-box li::before{content:"";width:4px;height:4px;background:var(--orange)}
.story{position:absolute;width:232px;font-size:8.3px;line-height:1.65;color:var(--grey-text)}
.story p+p{margin-top:10px}
.panel-head{font-size:21px;font-weight:700;line-height:1.2}
.panel-text{font-size:8.6px;line-height:1.4;margin-top:12px}
.year{position:absolute;left:76px;font-size:10px;font-weight:700;color:var(--blue);display:flex;align-items:center;gap:5px}
.year i{width:9px;height:9px;border-radius:50%;background:var(--orange)}
.seg{position:absolute;height:29px;font-size:7px;color:#fff;display:flex;align-items:center;justify-content:center}
.seg.o{background:var(--orange)}
.seg.b{background:var(--blue)}
.axis-label{position:absolute;top:240px;font-size:7px;color:var(--grey-text);transform:translateX(-50%)}
.tl-legend{position:absolute;top:262px;width:95px}
.tl-legend h5{font-size:6.5px;font-weight:700;color:var(--blue)}
.tl-legend h5.alt{color:var(--orange)}
.tl-legend p{font-size:4.5px;color:var(--grey-text);line-height:1.35}
.step{position:absolute;left:74px;width:160px}
.step b{position:absolute;left:0;top:0;width:20px;height:20px;background:var(--orange);color:#fff;font-size:12px;display:flex;align-items:center;justify-content:center;border:2px solid #fbd0b0}
.step h5{margin-left:28px;font-size:8px;font-weight:600;color:var(--blue)}
.step p{margin-left:28px;font-size:4.5px;color:var(--grey-text);line-height:1.4;margin-top:2px}
.phone{position:absolute;width:69px;height:145px;border:2px solid #222;border-radius:8px;background:#fff;padding:20px 6px 0}
.phone::before{content:"";position:absolute;left:20px;top:0;width:25px;height:4px;background:#222;border-radius:0 0 4px 4px}
.phone h5{font-size:7.5px;font-weight:700;color:var(--blue);line-height:1.15}
.phone .glyph{width:14px;height:10px;border:1.5px solid var(--orange);border-radius:2px;margin:10px auto 8px}
.phone p{font-size:3.6px;color:var(--grey-text);line-height:1.35}
.member{position:absolute;top:166px;width:80px;text-align:center}
.member .cap{height:38px;background:var(--orange)}
.member .avatar{width:46px;height:46px;border-radius:50%;border:3px solid #fff;margin:-26px auto 0;background:linear-gradient(160deg,#c7cdd6,#7d8794);box-shadow:0 0 0 1px #ddd}
.member h5{font-size:9px;font-weight:700;color:var(--orange);margin-top:8px}
.member p{font-size:4.2px;color:var(--grey-text);line-height:1.4;margin-top:3px}
.contact-line{position:absolute;left:296px;font-size:13px;color:#fff;display:flex;align-items:center;gap:6px}
.contact-line i{width:13px;height:13px;border-radius:50%;background:var(--orange);display:flex;align-items:center;justify-content:center}
</style>
</head>
<body>
<main class="board">

<!-- 1 Title -->
<section class="slide" style="left:58px;top:66px">
  <div class="rail light"><span>www.veltraconsulting.example</span></div>
  <div class="photo" role="img" aria-label="Classroom photo of children raising hands, blue duotone" style="left:50px;top:0;width:330px;height:338px;background:linear-gradient(135deg,#6f9fd0,#3d74b1 55%,#2a5c98)"></div>
  <div class="abs" style="left:64px;top:12px;width:17px;height:17px;background:var(--orange)"></div>
  <div class="abs" style="left:410px;top:78px;font-size:33px;font-weight:700;color:var(--grey-text);line-height:1">Veltra<br>Consulting</div>
  <div class="abs" style="left:323px;top:192px;width:277px;height:80px;background:var(--blue)"></div>
  <div class="abs" style="left:323px;top:192px;width:17px;height:80px;background:var(--orange)"></div>
  <div class="abs" style="left:354px;top:208px;color:#fff;font-size:20px;font-weight:700;line-height:1.25">Presentation<br>Business <span style="color:var(--orange)">Marketing</span></div>
  <div class="deco" style="left:500px;top:300px"></div>
</section>

<!-- 2 Contents -->
<section class="slide" style="left:676px;top:66px">
  <div class="rail"><span>www.veltraconsulting.example</span></div>
  <div class="brand">Veltra Consulting</div>
  <h2 class="title" style="left:64px;top:28px">Contents</h2>
  <div class="rule" style="left:64px;top:60px"></div>
  <div class="toc-item" style="left:74px;top:114px"><h3><b>1.</b>Lorem ipsum</h3><p>Lorem ipsum dolor sit amet, consectetuer adipiscing elit, sed diam nonummy nibh euismod tincid</p></div>
  <div class="toc-item" style="left:74px;top:174px"><h3><b>2.</b>Lorem ipsum</h3><p>Lorem ipsum dolor sit amet, consectetuer adipiscing elit, sed diam nonummy nibh euismod tincid</p></div>
  <div class="toc-item" style="left:74px;top:228px"><h3><b>3.</b>Lorem ipsum</h3><p>Lorem ipsum dolor sit amet, consectetuer adipiscing elit, sed diam nonummy nibh euismod tincid</p></div>
  <div class="toc-item" style="left:315px;top:114px"><h3><b>4.</b>Lorem ipsum</h3><p>Lorem ipsum dolor sit amet, consectetuer adipiscing elit, sed diam nonummy nibh euismod tincid</p></div>
  <div class="toc-item" style="left:315px;top:174px"><h3><b>5.</b>Lorem ipsum</h3><p>Lorem ipsum dolor sit amet, consectetuer adipiscing elit, sed diam nonummy nibh euismod tincid</p></div>
  <div class="toc-item" style="left:315px;top:228px"><h3><b>6.</b>Lorem ipsum</h3><p>Lorem ipsum dolor sit amet, consectetuer adipiscing elit, sed diam nonummy nibh euismod tincid</p></div>
  <div class="deco" style="left:510px;top:300px"></div>
</section>

<!-- 3 Our Company -->
<section class="slide" style="left:1297px;top:66px">
  <div class="rail"><span>www.veltraconsulting.example</span></div>
  <div class="brand">Veltra Consulting</div>
  <h2 class="title" style="left:66px;top:30px">Our<br>Company</h2>
  <div class="body" style="left:66px;top:110px;width:212px">
    <p>Lorem ipsum dolor sit amet, consectetuer adipiscing elit, sed diam nonummy nibh euismod tincidunt ut laoreet dolore magna aliquam erat volutpat. Ut wisi enim ad minim veniam, quis nostrud exerci tation ullamcorper suscipit lobortis nisl ut aliquip ex ea commodo consequat. Duis autem vel eum iriure dolor in hendrerit in</p>
    <p>Lorem ipsum dolor sit amet, consectetuer adipiscing elit, sed diam nonummy nibh euismod tincidunt ut laoreet dolore magna aliquam erat volutpat. Ut wisi enim ad minim veniam, quis nostrud exerci tation ullamcorper suscipit lobortis nisl ut aliquip ex ea commodo consequat. Duis autem vel eum iriure dolor in hendrerit in Lorem ipsum dolor sit amet, consectetuer adipiscing elit, sed diam nonummy nibh euismod tincidunt ut laoreet dolore magna aliquam erat volutpat. Ut wisi enim ad minim veniam, quis nostrud exerci tation ullamcorper suscipit lobortis nisl ut aliquip ex ea commodo</p>
  </div>
  <div class="badge" style="left:342px;top:62px"><i>✓</i></div>
  <div class="badge" style="left:479px;top:62px"><i>◎</i></div>
  <div class="badge" style="left:342px;top:179px"><i>$</i></div>
  <div class="badge" style="left:479px;top:179px"><i>↻</i></div>
  <div class="feature" style="left:317px;top:118px"><h4>LOREM IPSUM</h4><p>Lorem ipsum dolor sit amet, consectetuer adipiscing elit, sed diam nonummy nibh euismod tincid</p></div>
  <div class="feature" style="left:454px;top:118px"><h4 class="alt">LOREM IPSUM</h4><p>Lorem ipsum dolor sit amet, consectetuer adipiscing elit, sed diam nonummy nibh euismod tincid</p></div>
  <div class="feature" style="left:317px;top:235px"><h4 class="alt">LOREM IPSUM</h4><p>Lorem ipsum dolor sit amet, consectetuer adipiscing elit, sed diam nonummy nibh euismod tincid</p></div>
  <div class="feature" style="left:454px;top:235px"><h4>LOREM IPSUM</h4><p>Lorem ipsum dolor sit amet, consectetuer adipiscing elit, sed diam nonummy nibh euismod tincid</p></div>
  <div class="deco" style="left:510px;top:300px"></div>
</section>

<!-- 4 Founder Profile -->
<section class="slide" style="left:58px;top:424px">
  <div class="rail"><span>www.veltraconsulting.example</span></div>
  <div class="brand">Veltra Consulting</div>
  <h2 class="title" style="left:58px;top:34px">Founder<br>Profile</h2>
  <div class="rule" style="left:58px;top:88px"></div>
  <div class="body" style="left:60px;top:120px;width:164px">
    <p>Lorem ipsum dolor sit amet, consectetuer adipiscing elit, sed diam nonummy nibh euismod tincidunt ut laoreet dolore magna aliquam erat volutpat. Ut wisi enim ad minim veniam, quis nostrud exerci tation ullamcorper suscipit lobortis nisl ut aliquip ex ea commodo consequat. Duis autem vel eum iriure dolor in hendrerit in</p>
    <p>Lorem ipsum dolor sit amet, consectetuer adipiscing elit, sed diam nonummy nibh euismod tincidunt ut laoreet dolore magna aliquam erat volutpat. Ut wisi enim ad minim veniam, quis nostrud exerci tation ullamcorper suscipit lobortis nisl ut aliquip ex ea commodo consequat. Duis autem vel eum iriure dolor in hendrerit in</p>
  </div>
  <div class="abs" style="left:246px;top:60px;width:24px;height:24px;background:var(--orange)"></div>
  <div class="photo" role="img" aria-label="Team photo of colleagues stacking hands over a table" style="left:253px;top:67px;width:347px;height:231px;background:linear-gradient(140deg,#d9c7b6,#b99b85 45%,#8d7a72 80%,#e6e2dc)"></div>
  <div class="deco" style="left:500px;top:305px"></div>
</section>

<!-- 5 Company Education -->
<section class="slide" style="left:676px;top:424px;background:var(--blue)">
  <div class="rail" style="background:var(--blue-deep)"><span>www.veltraconsulting.example</span></div>
  <div class="brand on-blue">Veltra Consulting</div>
  <div class="abs" style="left:268px;top:-48px;width:88px;height:88px;border-radius:50%;background:var(--sky)"></div>
  <div class="abs" style="left:498px;top:300px;width:86px;height:86px;border-radius:50%;background:var(--sky)"></div>
  <h2 class="abs" style="left:52px;top:20px;color:#fff;font-size:17px;font-weight:700">Company Education</h2>
  <div class="rule" style="left:52px;top:49px;width:26px"></div>
  <svg class="abs" style="left:100px;top:80px" width="410" height="170" viewBox="0 0 410 170">
    <path d="M110 75 L130 75 M125 150 L168 72 M246 75 L266 75 M262 150 L306 72" stroke="#fff" stroke-width="3" fill="none"/>
    <circle cx="110" cy="50" r="5" fill="#fff"/><circle cx="148" cy="125" r="5" fill="#fff"/>
    <circle cx="246" cy="50" r="5" fill="#fff"/><circle cx="285" cy="125" r="5" fill="#fff"/>
  </svg>
  <div class="edu-box" style="left:113px;top:90px"><svg width="14" height="16" viewBox="0 0 14 16"><path d="M7 1a5 5 0 0 0-3 9v2h6v-2a5 5 0 0 0-3-9zM5 14h4" stroke="#f07f2d" stroke-width="1.5" fill="none"/></svg><h4>IDEA</h4><p>Lorem ipsum dolor sit amet, consectetuer adipiscing elit, sed diam nonummy nibh euismod tincidunt ut laoreet dolore magna aliquam erat volutpat. Ut wisi enim ad minim veniam, quis nostrud exerci tation ullamcorper suscipit lobortis nisl ut aliquip ex</p></div>
  <div class="edu-box" style="left:248px;top:90px"><svg width="16" height="12" viewBox="0 0 16 12"><rect x="1" y="1" width="14" height="10" stroke="#f07f2d" stroke-width="1.5" fill="none"/><path d="M1 1l7 6 7-6" stroke="#f07f2d" stroke-width="1.5" fill="none"/></svg><h4>PROMOTION</h4><p>Lorem ipsum dolor sit amet, consectetuer adipiscing elit, sed diam nonummy nibh euismod tincidunt ut laoreet dolore magna aliquam erat volutpat. Ut wisi enim ad minim veniam, quis nostrud exerci tation ullamcorper suscipit lobortis nisl ut aliquip ex</p></div>
  <div class="edu-box" style="left:385px;top:90px"><svg width="14" height="14" viewBox="0 0 14 14"><path d="M1 1v12h12M3 10l4-4 2 2 4-5" stroke="#f07f2d" stroke-width="1.5" fill="none"/></svg><h4>GROWTH</h4><p>Lorem ipsum dolor sit amet, consectetuer adipiscing elit, sed diam nonummy nibh euismod tincidunt ut laoreet dolore magna aliquam erat volutpat. Ut wisi enim ad minim veniam, quis nostrud exerci tation ullamcorper suscipit lobortis nisl ut aliquip ex</p></div>
  <svg class="abs" style="left:560px;top:90px" width="10" height="38"><g fill="#fff"><circle cx="2" cy="3" r="1.6"/><circle cx="8" cy="3" r="1.6"/><circle cx="2" cy="13" r="1.6"/><circle cx="8" cy="13" r="1.6"/><circle cx="2" cy="23" r="1.6"/><circle cx="8" cy="23" r="1.6"/><circle cx="2" cy="33" r="1.6"/><circle cx="8" cy="33" r="1.6"/></g></svg>
  <p class="abs" style="left:75px;top:257px;width:460px;text-align:center;color:#fff;font-size:6.6px;line-height:1.4">Lorem ipsum dolor sit amet, consectetuer adipiscing elit, sed diam nonummy nibh euismod tincidunt ut laoreet dolore magna aliquam erat volutpat. Ut wisi enim ad minim veniam, quis nostrud exerci tation ullamcorper suscipit lobortis nisl ut aliquip ex ea commodo consequat. Duis autem vel eum iriure dolor in hendrerit i</p>
</section>

<!-- 6 Text Here charts -->
<section class="slide" style="left:1297px;top:424px">
  <div class="rail"><span>www.veltraconsulting.example</span></div>
  <div class="brand">Veltra Consulting</div>
  <h2 class="title" style="left:68px;top:32px">Text Here</h2>
  <div class="rule" style="left:68px;top:66px"></div>
  <div class="body" style="left:68px;top:80px;width:200px;text-align:left;font-size:7.5px">
    <p>Lorem ipsum dolor sit amet, consectetuer adipiscing elit, sed diam nonummy nibh euismod tincidunt ut laoreet dolore magna aliquam erat volutpat. Ut wisi enim ad minim veniam</p>
    <p>quis nostrud exerci tation ullamcorper suscipit lobortis nisl ut aliquip ex ea commodo consequat. Duis autem vel eum iriure dolor in</p>
  </div>
  <svg class="abs" style="left:315px;top:62px" width="250" height="125" viewBox="0 0 250 125" font-family="Montserrat,Arial,sans-serif" font-size="6" fill="#555">
    <g stroke="#ddd" stroke-width=".6"><line x1="20" y1="5" x2="240" y2="5"/><line x1="20" y1="21.7" x2="240" y2="21.7"/><line x1="20" y1="38.3" x2="240" y2="38.3"/><line x1="20" y1="55" x2="240" y2="55"/><line x1="20" y1="71.7" x2="240" y2="71.7"/><line x1="20" y1="88.3" x2="240" y2="88.3"/><line x1="240" y1="5" x2="240" y2="105"/></g>
    <line x1="20" y1="5" x2="20" y2="105" stroke="#999" stroke-width=".6"/><line x1="20" y1="105" x2="240" y2="105" stroke="#999" stroke-width=".6"/>
    <g text-anchor="end"><text x="16" y="7">60</text><text x="16" y="24">50</text><text x="16" y="40">40</text><text x="16" y="57">30</text><text x="16" y="74">20</text><text x="16" y="90">10</text><text x="16" y="107">0</text></g>
    <rect x="42" y="38.3" width="6" height="66.7" fill="#0b4d8e"/><rect x="50" y="21.7" width="6" height="83.3" fill="#f07f2d"/>
    <rect x="95" y="86.7" width="6" height="18.3" fill="#f07f2d"/><rect x="103" y="46.7" width="6" height="58.3" fill="#0b4d8e"/>
    <rect x="148" y="10" width="6" height="95" fill="#f07f2d"/><rect x="156" y="83.3" width="6" height="21.7" fill="#0b4d8e"/>
    <rect x="201" y="18.3" width="6" height="86.7" fill="#0b4d8e"/><rect x="209" y="55" width="6" height="50" fill="#f07f2d"/>
    <g text-anchor="middle"><text x="49" y="116">JAN</text><text x="102" y="116">FEB</text><text x="155" y="116">MAR</text><text x="208" y="116">APR</text></g>
  </svg>
  <svg class="abs" style="left:78px;top:208px" width="205" height="92" viewBox="0 0 205 92" font-family="Montserrat,Arial,sans-serif" font-size="5" fill="#777">
    <g stroke="#e2e2e2" stroke-width=".5"><line x1="12" y1="5" x2="200" y2="5"/><line x1="12" y1="17" x2="200" y2="17"/><line x1="12" y1="29" x2="200" y2="29"/><line x1="12" y1="41" x2="200" y2="41"/><line x1="12" y1="53" x2="200" y2="53"/><line x1="12" y1="65" x2="200" y2="65"/><line x1="12" y1="77" x2="200" y2="77"/></g>
    <g text-anchor="end"><text x="9" y="7">60</text><text x="9" y="19">50</text><text x="9" y="31">40</text><text x="9" y="43">30</text><text x="9" y="55">20</text><text x="9" y="67">10</text><text x="9" y="79">0</text></g>
    <polyline points="18,62 38,77 58,45 78,14 98,24 118,52 138,42 158,28 178,63" fill="none" stroke="#0b4d8e" stroke-width="1"/>
    <polyline points="18,76 38,66 58,55 78,34 98,54 118,46 138,41 158,40 178,30" fill="none" stroke="#f07f2d" stroke-width="1"/>
    <g fill="#0b4d8e"><circle cx="18" cy="62" r="1.5"/><circle cx="78" cy="14" r="1.5"/><circle cx="118" cy="52" r="1.5"/><circle cx="158" cy="28" r="1.5"/><circle cx="178" cy="63" r="1.5"/></g>
    <g font-size="3.5" text-anchor="middle"><text x="18" y="86">TEXT 01</text><text x="38" y="86">TEXT 02</text><text x="58" y="86">TEXT 03</text><text x="78" y="86">TEXT 04</text><text x="98" y="86">TEXT 05</text><text x="118" y="86">TEXT 06</text><text x="138" y="86">TEXT 07</text><text x="158" y="86">TEXT 08</text><text x="178" y="86">TEXT 09</text></g>
  </svg>
  <div class="legend" style="left:318px;top:225px"><h5>Lorem ipsum</h5><p>Lorem ipsum dolor sit amet, consectetuer adipiscing elit, sed diam nonummy nibh euismod tincidunt ut laoreet</p></div>
  <div class="legend" style="left:448px;top:225px"><h5>Lorem ipsum</h5><p>Lorem ipsum dolor sit amet, consectetuer adipiscing elit, sed diam nonummy nibh euismod tincidunt ut laoreet</p></div>
  <div class="legend" style="left:318px;top:263px"><h5>Lorem ipsum</h5><p>Lorem ipsum dolor sit amet, consectetuer adipiscing elit, sed diam nonummy nibh euismod tincidunt ut laoreet</p></div>
  <div class="legend" style="left:448px;top:263px"><h5>Lorem ipsum</h5><p>Lorem ipsum dolor sit amet, consectetuer adipiscing elit, sed diam nonummy nibh euismod tincidunt ut laoreet</p></div>
  <div class="deco" style="left:510px;top:305px"></div>
</section>

<!-- 7 Market Opportunities -->
<section class="slide" style="left:58px;top:781px">
  <div class="rail"><span>www.veltraconsulting.example</span></div>
  <div class="brand">Veltra Consulting</div>
  <div class="deco" style="left:232px;top:-42px"></div>
  <h2 class="title" style="left:66px;top:46px;font-size:18px">Market<br>Opportunities.</h2>
  <div class="rule" style="left:66px;top:104px"></div>
  <div class="body" style="left:66px;top:128px;width:162px;text-align:left;font-size:7.2px">
    <p>Lorem ipsum dolor sit amet, consectetuer adipiscing elit, sed diam nonummy nibh euismod tincidunt ut laoreet dolore magna aliquam erat volutpat. Ut wisi enim ad minim veniam, quis nostrud exerci tation ullamcorper suscipit lobortis nisl ut aliquip ex ea commodo consequat. Duis autem vel eum iriure dolor in hendrerit i</p>
    <p>Lorem ipsum dolor sit amet, consectetuer adipiscing elit, sed diam nonummy nibh</p>
  </div>
  <p class="abs" style="left:290px;top:74px;font-size:7.5px;font-weight:600;color:#222">CONSECTETUER ADIPISCING</p>
  <svg class="abs" style="left:272px;top:90px" width="265" height="130" viewBox="0 0 265 130" font-family="Montserrat,Arial,sans-serif" font-size="7" fill="#333">
    <g stroke="#ccc" stroke-width=".6"><line x1="20" y1="7" x2="258" y2="7"/><line x1="20" y1="25" x2="258" y2="25"/><line x1="20" y1="43" x2="258" y2="43"/><line x1="20" y1="61" x2="258" y2="61"/><line x1="20" y1="79" x2="258" y2="79"/><line x1="20" y1="97" x2="258" y2="97"/><line x1="258" y1="7" x2="258" y2="115"/></g>
    <line x1="20" y1="7" x2="20" y2="115" stroke="#555" stroke-width=".7"/><line x1="20" y1="115" x2="258" y2="115" stroke="#555" stroke-width=".7"/>
    <g text-anchor="end"><text x="15" y="9">60</text><text x="15" y="27">50</text><text x="15" y="45">40</text><text x="15" y="63">30</text><text x="15" y="81">20</text><text x="15" y="99">10</text><text x="15" y="117">0</text></g>
    <rect x="50" y="17.8" width="25" height="97.2" fill="#0b4d8e"/>
    <rect x="100" y="57.4" width="25" height="57.6" fill="#f07f2d"/>
    <rect x="150" y="30.4" width="25" height="84.6" fill="#0b4d8e"/>
    <rect x="200" y="64.6" width="25" height="50.4" fill="#f07f2d"/>
    <g text-anchor="middle"><text x="62" y="127">JAN</text><text x="112" y="127">FEB</text><text x="162" y="127">MAR</text><text x="212" y="127">APR</text></g>
  </svg>
  <div class="legend" style="left:286px;top:244px"><h5 class="dot-orange" style="color:var(--blue)">Lorem ipsum</h5><p>Lorem ipsum dolor sit amet, consectetuer adipiscing elit, sed diam nonummy nibh euismod tincidunt ut laoreet</p></div>
  <div class="legend" style="left:416px;top:244px"><h5 class="dot-orange" style="color:var(--blue)">Lorem ipsum</h5><p>Lorem ipsum dolor sit amet, consectetuer adipiscing elit, sed diam nonummy nibh euismod tincidunt ut laoreet</p></div>
  <div class="deco" style="left:500px;top:305px"></div>
</section>

<!-- 8 Our Services -->
<section class="slide" style="left:676px;top:781px">
  <div class="rail"><span>www.veltraconsulting.example</span></div>
  <div class="brand">Veltra Consulting</div>
  <div class="abs" style="left:37px;top:0;width:268px;height:338px;background:var(--blue)"></div>
  <div class="num-circle" style="left:57px;top:62px">1</div>
  <div class="num-circle" style="left:57px;top:151px">2</div>
  <div class="num-circle" style="left:57px;top:236px">3</div>
  <p class="abs" style="left:107px;top:59px;width:170px;color:#fff;font-size:6.4px;line-height:1.3;text-align:justify">Lorem ipsum dolor sit amet, consectetuer adipiscing elit, sed diam nonummy nibh euismod tincidunt ut laoreet dolore magna aliquam erat volutpat. Ut wisi enim ad minim veniam, quis nostrud exerci tation ullamcorper</p>
  <p class="abs" style="left:107px;top:145px;width:170px;color:#fff;font-size:6.4px;line-height:1.3">ullamcorper suscipit lobortis nisl ut aliquip ex ea commodo consequat. Duis autem vel eum iriure dolor in hendrerit in vulputate velit esse<br><br>molestie consequat, vel illum dolore eu feugiat nulla facilisis at vero eros et accumsan et iusto</p>
  <p class="abs" style="left:107px;top:236px;width:170px;color:#fff;font-size:6.4px;line-height:1.3;text-align:justify">Lorem ipsum dolor sit amet, consectetuer adipiscing elit, sed diam nonummy nibh euismod tincidunt ut laoreet dolore magna aliquam erat volutpat. Ut wisi enim ad minim veniam, quis nostrud exerci tation ullamcorper</p>
  <h2 class="title" style="left:372px;top:76px">Our Services</h2>
  <div class="rule" style="left:424px;top:110px;width:30px"></div>
  <div class="photo" role="img" aria-label="Photo of two women in a meeting, soft office light" style="left:305px;top:124px;width:295px;height:198px;background:linear-gradient(110deg,#7f8f84,#b9b2a8 45%,#e4e2dd 70%,#9a9490)"></div>
  <svg class="abs" style="left:284px;top:276px" width="42" height="12"><g fill="#f07f2d"><circle cx="2" cy="2" r="1.5"/><circle cx="10" cy="2" r="1.5"/><circle cx="18" cy="2" r="1.5"/><circle cx="26" cy="2" r="1.5"/><circle cx="34" cy="2" r="1.5"/><circle cx="2" cy="9" r="1.5"/><circle cx="10" cy="9" r="1.5"/><circle cx="18" cy="9" r="1.5"/><circle cx="26" cy="9" r="1.5"/><circle cx="34" cy="9" r="1.5"/></g></svg>
</section>

<!-- 9 Our Goal -->
<section class="slide" style="left:1297px;top:781px">
  <div class="rail"><span>www.veltraconsulting.example</span></div>
  <div class="brand">Veltra Consulting</div>
  <div class="deco" style="left:220px;top:-42px"></div>
  <h2 class="title" style="left:68px;top:24px">Our Goal</h2>
  <div class="rule" style="left:68px;top:56px"></div>
  <p class="goal-item" style="top:80px"><b>Lorem Ipsum :</b> dolor sit amet, consectetuer adipiscing elit, sed diam nonummy nibh euismod tincidunt ut laoreet dolore magna aliquam erat volutpat. Ut wisi enim ad minim veniam,</p>
  <p class="goal-item o" style="top:127px"><b>Lorem Ipsum :</b> dolor sit amet, consectetuer adipiscing elit, sed diam nonummy nibh euismod tincidunt ut laoreet dolore magna aliquam erat volutpat. Ut wisi enim ad minim veniam,</p>
  <p class="goal-item" style="top:174px"><b>Lorem Ipsum :</b> dolor sit amet, consectetuer adipiscing elit, sed diam nonummy nibh euismod tincidunt ut laoreet dolore</p>
  <p class="goal-item o" style="top:210px"><b>Lorem Ipsum :</b> dolor sit amet, consectetuer adipiscing elit, sed diam nonummy nibh euismod tincidunt ut laoreet dolore magna aliquam erat volutpat. Ut wisi enim ad minim veniam,</p>
  <p class="goal-item" style="top:256px"><b>Lorem Ipsum :</b> dolor sit amet, consectetuer adipiscing elit, sed diam nonummy nibh euismod tincidunt ut laoreet dolore</p>
  <div class="goal-box">
    <h3>WHAT'S A DOMAIN? IT'S<br>THAT NAME UP<br><em>IN THE ADDRESS BAR.</em></h3>
    <ul><li>Fits your business or products</li><li>Is easy to spell and remember</li><li>Fits your business or products</li><li>Is easy to spell and remember</li><li>Fits your business or products</li><li>Is easy to spell and remember</li></ul>
  </div>
  <div class="deco" style="left:510px;top:305px"></div>
</section>

<!-- 10 Our Story -->
<section class="slide" style="left:58px;top:1140px">
  <div class="rail"><span>www.veltraconsulting.example</span></div>
  <div class="brand">Veltra Consulting</div>
  <div class="deco" style="left:232px;top:-42px"></div>
  <h2 class="title" style="left:62px;top:24px">Our Story</h2>
  <div class="rule" style="left:62px;top:56px"></div>
  <div class="story" style="left:70px;top:82px">
    <p>Lorem ipsum dolor sit amet, consectetuer adipiscing elit, sed diam ut aliquip ex ea commodo consequat. Duis autem vel eum iriure dolor in hendrerit in</p>
    <p>Lorem ipsum dolor sit amet, consectetuer adipiscing elit, sed diam nonummy nibh euismod tincidunt ut laoreet ea commodo consequat. Duis autem Lorem ipsum dolor sit amet, consectetuer adipiscing elit, sed diam nonummy nibh euismod tincidunt ut laoreet ea commodo consequat. Duis autem</p>
    <p>Lorem ipsum dolor sit amet, consectetuer adipiscing elit, sed diam ut aliquip ex ea commodo consequat. Duis autem vel eum iriure dolor in hendrerit in</p>
  </div>
  <div class="story" style="left:324px;top:82px">
    <p>Lorem ipsum dolor sit amet, consectetuer adipiscing elit, sed diam ut aliquip ex ea commodo consequat. Duis autem vel eum iriure dolor in hendrerit in</p>
    <p>Lorem ipsum dolor sit amet, consectetuer adipiscing elit, sed diam nonummy nibh euismod tincidunt ut laoreet ea commodo consequat. Duis autem Lorem ipsum dolor sit amet, consectetuer adipiscing elit, sed diam nonummy nibh euismod tincidunt ut laoreet ea commodo consequat. Duis autem</p>
    <p>Lorem ipsum dolor sit amet, consectetuer adipiscing elit, sed diam ut aliquip ex ea commodo consequat. Duis autem vel eum iriure dolor in hendrerit in</p>
  </div>
  <div class="deco" style="left:500px;top:305px"></div>
</section>

<!-- 11 Two panels -->
<section class="slide" style="left:676px;top:1140px">
  <div class="rail"><span>www.veltraconsulting.example</span></div>
  <div class="brand">Veltra Consulting</div>
  <div class="deco" style="left:232px;top:-42px"></div>
  <h2 class="title" style="left:60px;top:24px">Text Here</h2>
  <div class="rule" style="left:60px;top:56px"></div>
  <div class="num-circle" style="left:85px;top:108px">1</div>
  <div class="abs" style="left:137px;top:102px;width:160px;color:var(--blue)">
    <h3 class="panel-head">Lorem ipsum dolor sit amet</h3>
    <p class="panel-text" style="color:var(--grey-text)">Praesent bibendum at risus ac blandit. In eu risus vel felis elementum venenatis vitae sed lacus. Curabitur vel erat urna.</p>
  </div>
  <div class="abs" style="left:323px;top:94px;width:197px;height:175px;background:var(--blue)"></div>
  <div class="num-circle" style="left:304px;top:108px">2</div>
  <div class="abs" style="left:355px;top:100px;width:155px;color:#fff">
    <h3 class="panel-head">Lorem ipsum dolor sit amet</h3>
    <p class="panel-text">Praesent bibendum at risus ac blandit. In eu risus vel felis elementum venenatis vitae sed lacus. Curabitur vel erat urna.</p>
  </div>
  <div class="deco" style="left:510px;top:305px"></div>
</section>

<!-- 12 Our Timeline -->
<section class="slide" style="left:1297px;top:1140px">
  <div class="rail"><span>www.veltraconsulting.example</span></div>
  <div class="brand">Veltra Consulting</div>
  <div class="deco" style="left:220px;top:-42px"></div>
  <h2 class="title" style="left:56px;top:22px">Our Timeline</h2>
  <div class="rule" style="left:56px;top:54px"></div>
  <div class="year" style="top:110px"><i></i>2019</div>
  <div class="year" style="top:152px"><i></i>2020</div>
  <div class="year" style="top:195px"><i></i>2021</div>
  <div class="abs" style="left:142px;top:86px;width:1.5px;height:144px;background:#333"></div>
  <div class="abs" style="left:142px;top:228px;width:362px;height:1.5px;background:#333"></div>
  <div class="seg o" style="left:143px;top:102px;width:54px">20%</div>
  <div class="seg b" style="left:197px;top:102px;width:73px">40%</div>
  <div class="seg o" style="left:270px;top:102px;width:50px">10%</div>
  <div class="seg b" style="left:320px;top:102px;width:183px">90%</div>
  <div class="seg o" style="left:143px;top:144px;width:128px">50%</div>
  <div class="seg b" style="left:271px;top:144px;width:89px">30%</div>
  <div class="seg o" style="left:360px;top:144px;width:73px">20%</div>
  <div class="seg b" style="left:433px;top:144px;width:70px">20%</div>
  <div class="seg b" style="left:143px;top:186px;width:74px">30%</div>
  <div class="seg o" style="left:217px;top:186px;width:106px">60%</div>
  <div class="seg b" style="left:323px;top:186px;width:37px">10%</div>
  <div class="seg o" style="left:360px;top:186px;width:143px">70%</div>
  <svg class="abs" style="left:138px;top:224px" width="370" height="10"><g fill="#333"><circle cx="5" cy="5" r="2.5"/><circle cx="41" cy="5" r="2.5"/><circle cx="77" cy="5" r="2.5"/><circle cx="113" cy="5" r="2.5"/><circle cx="149" cy="5" r="2.5"/><circle cx="185" cy="5" r="2.5"/><circle cx="221" cy="5" r="2.5"/><circle cx="257" cy="5" r="2.5"/><circle cx="293" cy="5" r="2.5"/><circle cx="329" cy="5" r="2.5"/><circle cx="365" cy="5" r="2.5"/></g></svg>
  <span class="axis-label" style="left:143px">0%</span><span class="axis-label" style="left:179px">10%</span><span class="axis-label" style="left:215px">20%</span><span class="axis-label" style="left:251px">30%</span><span class="axis-label" style="left:287px">40%</span><span class="axis-label" style="left:323px">50%</span><span class="axis-label" style="left:359px">60%</span><span class="axis-label" style="left:395px">70%</span><span class="axis-label" style="left:431px">80%</span><span class="axis-label" style="left:467px">90%</span><span class="axis-label" style="left:503px">100%</span>
  <div class="tl-legend" style="left:137px"><h5>LOREM IPSUM</h5><p>Lorem ipsum dolor sit amet, consectetuer adipiscing elit, sed diam nonummy nibh euismod tincid</p></div>
  <div class="tl-legend" style="left:234px"><h5 class="alt">LOREM IPSUM</h5><p>Lorem ipsum dolor sit amet, consectetuer adipiscing elit, sed diam nonummy nibh euismod tincid</p></div>
  <div class="tl-legend" style="left:337px"><h5>LOREM IPSUM</h5><p>Lorem ipsum dolor sit amet, consectetuer adipiscing elit, sed diam nonummy nibh euismod tincid</p></div>
  <div class="tl-legend" style="left:440px"><h5 class="alt">LOREM IPSUM</h5><p>Lorem ipsum dolor sit amet, consectetuer adipiscing elit, sed diam nonummy nibh euismod tincid</p></div>
</section>

<!-- 13 Text with screens -->
<section class="slide" style="left:58px;top:1502px">
  <div class="rail"><span>www.veltraconsulting.example</span></div>
  <div class="brand">Veltra Consulting</div>
  <div class="deco" style="left:232px;top:-42px"></div>
  <h2 class="title" style="left:62px;top:22px">Text Here</h2>
  <div class="rule" style="left:62px;top:54px"></div>
  <div class="body" style="left:64px;top:70px;width:180px;text-align:left;font-size:6.8px;line-height:1.35">
    <p>Lorem ipsum dolor sit amet, consectetuer adipiscing elit, sed diam nonummy nibh euismod tincidunt ut laoreet dolore magna aliquam erat volutpat. Ut wisi enim ad minim veniam,</p>
    <p>Lorem ipsum dolor sit amet, consectetuer adipiscing elit, sed diam nonummy nibh euismod tincidunt ut laoreet dolore</p>
  </div>
  <div class="step" style="top:180px"><b>1.</b><h5>Lorem ipsum</h5><p>Lorem ipsum dolor sit amet, consectetuer adipiscing elit, sed diam nonummy nibh</p></div>
  <div class="step" style="top:225px"><b>2.</b><h5>Lorem ipsum</h5><p>Lorem ipsum dolor sit amet, consectetuer adipiscing elit, sed diam nonummy nibh</p></div>
  <div class="step" style="top:270px"><b>3.</b><h5>Lorem ipsum</h5><p>Lorem ipsum dolor sit amet, consectetuer adipiscing elit, sed diam nonummy nibh</p></div>
  <div class="phone" style="left:284px;top:56px"><h5>Lorem ipsum dolor</h5><div class="glyph"></div><p>To introduce the students to the changing landscape of marketing and equip them with knowledge and skills to navigate the digital marketing world.</p></div>
  <div class="phone" style="left:371px;top:100px"><h5>Dolor sit amet, conse</h5><div class="glyph"></div><p>You will learn concepts and ideas in digital marketing as well as how to use different tools and strategies to optimise your digital marketing campaigns.</p></div>
  <div class="phone" style="left:458px;top:148px"><h5>Consec</h5><div class="glyph"></div><p>You are required to pass 80% of the evaluation test to obtain the certificate. The evaluation test can only be taken 3 times.</p></div>
</section>

<!-- 14 Our Team -->
<section class="slide" style="left:676px;top:1502px">
  <div class="rail"><span>www.veltraconsulting.example</span></div>
  <div class="brand">Veltra Consulting</div>
  <div class="deco" style="left:232px;top:-42px"></div>
  <h2 class="title" style="left:57px;top:22px">Our Team</h2>
  <div class="rule" style="left:57px;top:54px"></div>
  <div class="body" style="left:57px;top:64px;width:510px;font-size:7.3px;line-height:1.3;text-align:left">
    <p>Lorem ipsum dolor sit amet, consectetuer adipiscing elit, sed diam nonummy nibh euismod tincidunt ut laoreet dolore magna aliquam erat volutpat. Ut wisi enim ad minim veniam, quis nostrud exerci tation ullamcorper suscipit lobortis nisl ut aliquip ex ea commodo consequat. Duis autem vel eum iriure dolor in hendrerit in vulputate velit esse molestie consequat, vel illum dolore eu feugiat nulla facilisis at vero eros et accumsan et iusto odio dignissim qui blandit praesent luptatum zzril delenit augue duis dolore te feugait nulla facilisi.</p>
    <p>Lorem ipsum dolor sit amet, cons ectetuer adipiscing elit, sed diam nonummy nibh euismod tincidunt ut laoreet dolore magna</p>
  </div>
  <div class="member" style="left:68px"><div class="cap"></div><div class="avatar" role="img" aria-label="Portrait of team member"></div><h5>TOM AVERY</h5><p>Ipsum dolor sit amet, cons ectetuer adipiscing elit, sed diam nonummy nibh euismod tincidunt ut laoreet dolore magna aliquam erat volutpat. Ut wisi enim ad minim veniam</p></div>
  <div class="member" style="left:206px"><div class="cap"></div><div class="avatar" role="img" aria-label="Portrait of team member"></div><h5>MARA LIND</h5><p>Ipsum dolor sit amet, cons ectetuer adipiscing elit, sed diam nonummy nibh euismod tincidunt ut laoreet dolore magna aliquam erat volutpat. Ut wisi enim ad minim veniam</p></div>
  <div class="member" style="left:341px"><div class="cap"></div><div class="avatar" role="img" aria-label="Portrait of team member"></div><h5>TOM AVERY</h5><p>Ipsum dolor sit amet, cons ectetuer adipiscing elit, sed diam nonummy nibh euismod tincidunt ut laoreet dolore magna aliquam erat volutpat. Ut wisi enim ad minim veniam</p></div>
  <div class="member" style="left:480px"><div class="cap"></div><div class="avatar" role="img" aria-label="Portrait of team member"></div><h5>MARA LIND</h5><p>Ipsum dolor sit amet, cons ectetuer adipiscing elit, sed diam nonummy nibh euismod tincidunt ut laoreet dolore magna aliquam erat volutpat. Ut wisi enim ad minim veniam</p></div>
</section>

<!-- 15 Contact -->
<section class="slide" style="left:1297px;top:1502px;background:var(--blue)">
  <div class="rail light"><span>www.veltraconsulting.example</span></div>
  <div class="abs" style="left:265px;top:-95px;width:160px;height:160px;border-radius:50%;background:var(--sky)"></div>
  <div class="abs" style="left:565px;top:30px;width:90px;height:90px;border-radius:50%;background:var(--sky)"></div>
  <div class="abs" style="left:405px;top:288px;width:150px;height:150px;border-radius:50%;background:var(--sky)"></div>
  <div class="abs" style="left:175px;top:88px;font-size:44px;font-weight:700;color:#b9c6d8;line-height:.95">Veltra<br>Consulting</div>
  <div class="abs" style="left:108px;top:210px;font-size:24px;font-weight:500;color:#fff;letter-spacing:.5px">CONTACT <b style="color:var(--orange);font-weight:800">US</b></div>
  <div class="contact-line" style="top:204px"><i><svg width="7" height="7" viewBox="0 0 10 10"><path d="M2 1l2 2-1 1.5c.8 1.5 1.8 2.5 3.5 3.5L8 6l2 2-1.5 1.5C5 9 1 5 .5 1.5z" fill="#fff"/></svg></i>+44 20 7946 0321</div>
  <div class="contact-line" style="top:228px"><i><svg width="7" height="6" viewBox="0 0 10 8"><rect x=".5" y=".5" width="9" height="7" fill="none" stroke="#fff"/><path d="M.5.5L5 4.5 9.5.5" fill="none" stroke="#fff"/></svg></i>info@veltraconsulting.example</div>
</section>

</main>
</body>
</html>
```